Accounting business needs a great flyer

I need a flyer for my new business "Ledgerline". I am an individual accountant working for himself on the Sunshine Coast in Queensland Australia. I would like to see designs that communicate reliability and trust. I believe my point of difference is that I am always available to my clients and I will cap my number of clients to ensure I can service them properly.
The main point I want to convey is that most of the time junior employees with little to no experience or unqualified employees do the tax work for the clients and a senior accountant quickly checks the work at the end but never gets to really know the clients business. Accountants in general seem to have a bad reputation for not responding to clients in a timely fashion, whether by email or phone. This is where I intend to differentiate myself. . I have also included some logo's that should go on the flyer.

Target Market(s)

Every small business

Industry/Entity Type

Public Accounting

Requirements
Must have
• Web address: www.ledgerline.com.au
Phone number: 0417 582 396
Attached logos
Reference to: "Do you know who is actually doing your tax?"
Other accounting firms - use junior unqualified staff
- outsource to cheap labour countries
- use tax consultants who sometimes have had only 2 weeks training.
At Ledgerline, a highly qualified CPA with a Masters in Taxation does your work from start to finish.
**I don't need it to say exactly this but I want the theme of the flyer to have these points in it.
Nice to have
• Something different

```html
<!DOCTYPE html>
<html lang="en">
<head>
<meta charset="utf-8">
<title>Ledgerline – Flyer</title>
<link rel="stylesheet" href="https://fonts.googleapis.com/css2?family=Montserrat:wght@300;400;500;600;700;800;900&family=Oswald:wght@600;700&display=swap">
<style>
  :root{
    --navy:#16327a;
    --navy-soft:#2b4a8f;
    --navy-text:#1a2f73;
    --yellow:#f9b800;
    --ink:#222327;
    --charcoal:#2d2e32;
    --grey-text:#3a3b40;
    --pale:#f1f2f4;
    --stage:#e6e7ea;
    --white:#ffffff;
    --cyan:#1ab4e8;
    --badge-blue:#0a5cab;
    --badge-gold:#f7d417;
  }
  *{box-sizing:border-box;margin:0;padding:0}
  html,body{width:990px;height:1200px;overflow:hidden;background:var(--stage)}
  body{font-family:"Montserrat",Arial,sans-serif;position:relative}

  .flyer{
    position:absolute;left:54px;top:30px;
    width:1224px;height:1584px;
    transform:scale(.72);transform-origin:0 0;
    background:var(--white);overflow:hidden;
    box-shadow:0 6px 30px rgba(0,0,0,.18);
  }
  .abs{position:absolute}
  .shapes{position:absolute;inset:0}

  /* brand */
  .brand-ring{position:absolute;left:198px;top:80px;width:134px;height:134px;border:5px solid var(--ink);border-radius:50%}
  .brand-name{position:absolute;left:60px;top:236px;width:410px;text-align:center;
    font-weight:500;font-size:44px;letter-spacing:11px;color:var(--ink);line-height:1}

  /* headline */
  .headline{color:var(--white);line-height:1;white-space:nowrap}
  .hl-know{left:247px;top:582px;font-size:58px;font-weight:700}
  .hl-actually{left:102px;top:652px;font-size:56px;font-weight:700}
  .hl-actually .light{font-weight:300}
  .hl-doing{left:96px;top:705px;font-size:128px;font-weight:800;color:var(--yellow);letter-spacing:-2px}
  .hl-tax{left:170px;top:810px;font-size:128px;font-weight:800;color:var(--yellow);letter-spacing:-2px}
  .hl-mark{left:690px;top:770px;font-size:205px;font-weight:900;color:var(--yellow)}

  /* competitor points */
  .rival-points{left:98px;top:972px;width:560px;list-style:none;color:var(--white);
    font-size:29px;font-weight:700;line-height:38px}
  .rival-points li{position:relative;padding-left:44px;margin-bottom:14px}
  .rival-points svg{position:absolute;left:0;top:7px;width:26px;height:26px;color:var(--yellow)}
  .rival-rail{left:111px;top:1006px;width:2px;height:100px;background:var(--yellow)}

  /* call to action */
  .cta-text{left:137px;top:1236px;color:var(--white);font-weight:800;text-align:left}
  .cta-request{font-size:30px;line-height:1}
  .cta-free{display:inline-block;margin-top:10px;border:2px solid var(--white);padding:2px 12px 0;
    font-size:58px;line-height:56px;color:var(--yellow);font-weight:900}
  .cta-consult{font-size:22px;margin-top:10px;line-height:1}

  .online-badge{left:462px;top:1216px;width:152px;text-align:center;
    font-family:"Oswald",Arial,sans-serif;font-weight:700;color:var(--navy-text);line-height:1}
  .online-badge .big{font-size:36px;display:block;letter-spacing:.5px}
  .online-badge .small{font-size:24px;display:block;margin-top:3px}

  /* contact */
  .phone-pill{left:92px;top:1446px;width:390px;height:56px;border-radius:28px;background:var(--charcoal);}
  .phone-icon{left:94px;top:1448px;width:52px;height:52px;border-radius:50%;background:var(--navy);
    border:3px solid var(--white);box-shadow:0 0 0 2px var(--navy)}
  .phone-number{left:162px;top:1450px;font-size:44px;font-weight:800;color:var(--white);line-height:48px}
  .web{left:99px;top:1512px;font-size:27px;letter-spacing:3.4px;color:var(--ink);font-weight:500;display:flex;align-items:center;gap:8px}
  .web b{color:var(--navy-text);font-weight:700}
  .web svg{width:22px;height:22px;color:var(--navy-text)}

  /* right column */
  .promise{right:69px;top:912px;text-align:right;font-size:28px;line-height:35px;color:var(--navy-text);font-weight:700}
  .promise .light{font-weight:300;color:var(--grey-text)}
  .difference-band{left:772px;top:1135px;width:383px;height:42px}
  .difference-title{left:772px;top:1135px;width:383px;height:42px;line-height:42px;text-align:center;
    font-size:23px;font-weight:700;color:var(--yellow);padding-left:24px}
  .difference-list{right:69px;top:1192px;width:520px;list-style:none;text-align:right;
    font-size:20px;line-height:24.5px;color:var(--grey-text);font-weight:500}
  .difference-list li{margin-bottom:12px}
  .difference-list svg{width:19px;height:19px;vertical-align:-3px;margin-right:8px;color:var(--navy-text)}

  .accreditations{left:515px;top:1442px;width:405px;height:95px;border:2px solid #e4e5e8;border-radius:6px;background:var(--white)}
</style>
</head>
<body>
<svg width="0" height="0" style="position:absolute">
  <defs>
    <symbol id="tick" viewBox="0 0 26 26">
      <circle cx="13" cy="13" r="11" fill="none" stroke="currentColor" stroke-width="2"/>
      <polyline points="8,13.5 11.8,17 18,9.5" fill="none" stroke="currentColor" stroke-width="2.2" stroke-linecap="round" stroke-linejoin="round"/>
    </symbol>
  </defs>
</svg>

<main class="flyer">
  <svg class="shapes" viewBox="0 0 1224 1584" width="1224" height="1584">
    <defs>
      <linearGradient id="team-photo-tone" x1="0" y1="0" x2="1" y2="1">
        <stop offset="0" stop-color="#e8dccb"/>
        <stop offset=".45" stop-color="#7c9bb3"/>
        <stop offset="1" stop-color="#d7dde4"/>
      </linearGradient>
    </defs>
    <!-- soft background diamonds -->
    <rect x="-40" y="470" width="420" height="420" rx="80" fill="var(--pale)" transform="rotate(45 170 680)"/>
    <rect x="760" y="960" width="620" height="620" rx="90" fill="#f5f6f7" transform="rotate(45 1070 1270)"/>
    <!-- photo panel -->
    <path role="img" aria-label="Photo of three colleagues reviewing documents at a desk in a bright office"
      d="M717 0 H1224 V600 L1030 794 Q987 837 944 794 L500 340 Q467 306 500 268 Z" fill="url(#team-photo-tone)"/>
    <!-- navy diamond -->
    <rect x="7" y="512" width="750" height="750" rx="90" fill="var(--navy)" transform="rotate(45 382 887)"/>
    <rect x="0" y="500" width="460" height="460" rx="80" fill="var(--navy-soft)" opacity=".55" transform="rotate(45 230 730)"/>
    <!-- consultation tag -->
    <polygon points="99,1197 372,1232 327,1387 212,1397 239,1429 132,1407" fill="var(--charcoal)"/>
    <!-- online badge -->
    <g fill="var(--yellow)">
      <circle cx="537" cy="1292" r="80"/>
      <circle cx="537" cy="1206" r="14"/><circle cx="580" cy="1218" r="14"/><circle cx="611" cy="1249" r="14"/>
      <circle cx="623" cy="1292" r="14"/><circle cx="611" cy="1335" r="14"/><circle cx="580" cy="1366" r="14"/>
      <circle cx="537" cy="1378" r="14"/><circle cx="494" cy="1366" r="14"/><circle cx="463" cy="1335" r="14"/>
      <circle cx="451" cy="1292" r="14"/><circle cx="463" cy="1249" r="14"/><circle cx="494" cy="1218" r="14"/>
    </g>
    <!-- difference band -->
    <polygon points="772,1135 1154,1135 1154,1177 800,1177" fill="var(--navy)"/>
    <!-- yellow corner -->
    <path d="M897 1584 L1030 1465 Q1059 1440 1088 1465 L1224 1584 Z" fill="var(--yellow)"/>
  </svg>

  <div class="brand-ring" aria-hidden="true"></div>
  <div class="brand-name">LEDGERLINE</div>

  <div class="abs headline hl-know">Do you know</div>
  <div class="abs headline hl-actually"><span class="light">who is </span>actually</div>
  <div class="abs headline hl-doing">doing</div>
  <div class="abs headline hl-tax">your tax</div>
  <div class="abs headline hl-mark">?</div>

  <div class="abs rival-rail"></div>
  <ul class="abs rival-points">
    <li><svg><use href="#tick"/></svg>Other accounting firms often use junior or unqualified staff to prepare your tax or</li>
    <li><svg><use href="#tick"/></svg>Outsource to cheap labour countries</li>
  </ul>

  <div class="abs cta-text">
    <div class="cta-request">REQUEST A</div>
    <div class="cta-free">FREE</div>
    <div class="cta-consult">CONSULTATION</div>
  </div>

  <div class="abs online-badge">
    <span class="big">ONLINE</span>
    <span class="big">SERVICES</span>
    <span class="small">AVAILABLE</span>
  </div>

  <div class="abs phone-pill"></div>
  <div class="abs phone-icon">
    <svg viewBox="0 0 46 46" width="46" height="46"><path d="M16 12 l5 0 2 7 -3 3 q3 6 8 8 l3 -3 7 2 0 5 q-1 3 -4 3 q-20 -2 -21 -21 q0 -3 3 -4z" fill="none" stroke="#fff" stroke-width="2.4" stroke-linejoin="round"/></svg>
  </div>
  <div class="abs phone-number">0417 582 396</div>
  <div class="abs web">
    <svg viewBox="0 0 24 24"><circle cx="12" cy="12" r="10" fill="none" stroke="currentColor" stroke-width="2"/><ellipse cx="12" cy="12" rx="4.5" ry="10" fill="none" stroke="currentColor" stroke-width="1.6"/><line x1="2" y1="12" x2="22" y2="12" stroke="currentColor" stroke-width="1.6"/></svg>
    <span>www.<b>ledgerline</b>.com.au</span>
  </div>

  <div class="abs promise">
    <span class="light">At Ledgerline,</span><br>
    a Highly Qualified<br>
    CPA <span class="light">with a</span><br>
    Masters in Taxation<br>
    does your work <span class="light">from</span><br>
    Start to Finish.
  </div>

  <div class="abs difference-title">The Ledgerline difference:</div>
  <ul class="abs difference-list">
    <li><svg><use href="#tick"/></svg>I get to know your business</li>
    <li><svg><use href="#tick"/></svg>I am always available (no more waiting weeks<br>to hear back from your accountant)</li>
    <li><svg><use href="#tick"/></svg>I have years of experience in running<br>small businesses</li>
    <li><svg><use href="#tick"/></svg> I have fixed fees and don't send you<br>any surprise invoices</li>
    <li><svg><use href="#tick"/></svg>No outsourcing work</li>
  </ul>

  <div class="abs accreditations">
    <svg viewBox="0 0 405 95" width="401" height="91">
      <circle cx="58" cy="46" r="28" fill="#e9eaec" stroke="#c9cbd0" stroke-width="2"/>
      <rect x="108" y="10" width="104" height="71" fill="var(--badge-blue)"/>
      <rect x="212" y="10" width="64" height="71" fill="var(--badge-gold)"/>
      <circle cx="335" cy="46" r="37" fill="var(--cyan)"/>
    </svg>
  </div>
</main>
</body>
</html>
```